KORBALT

The business want a professional looking business card. We have a scetch we will add but want the extra upgrade, and would like more suggestions for variations of our business cards.

```html
<!DOCTYPE html>
<html lang="en">
<head>
<meta charset="utf-8">
<title>KORBALT Business Cards</title>
<link rel="stylesheet" href="https://fonts.googleapis.com/css2?family=Marcellus&family=Montserrat:wght@400;500&display=swap">
<style>
  :root {
    --card-bg: #25272d;
    --page-bg: #1f2125;
    --stage-bg: #2b2d32;
    --gold: #c9a456;
    --gold-soft: #b8954c;
  }
  * { margin: 0; padding: 0; box-sizing: border-box; }
  html, body { width: 1200px; height: 1064px; overflow: hidden; background: var(--page-bg); }
  .canvas { position: relative; width: 1200px; height: 1064px; }

  .card {
    position: absolute;
    width: 596px;
    height: 396px;
    background: var(--card-bg);
    color: var(--gold);
  }
  .card-frame {
    position: absolute;
    inset: 16px;
    border: 2px solid var(--gold);
  }

  /* Contact side */
  .company-title {
    position: absolute; left: 58px; top: 60px;
    font-family: "Marcellus", serif; font-size: 31px; letter-spacing: 0.5px;
  }
  .role {
    position: absolute; left: 58px; top: 110px;
    font-family: "Montserrat", sans-serif; font-size: 25px; font-weight: 400;
  }
  .person {
    position: absolute; left: 58px; top: 148px;
    font-family: "Montserrat", sans-serif; font-size: 17px; font-weight: 400;
  }
  .contacts { position: absolute; left: 56px; top: 243px; list-style: none; }
  .contacts li {
    display: flex; align-items: center; height: 35px;
    font-family: "Montserrat", sans-serif; font-size: 20px;
  }
  .contacts svg { width: 22px; height: 22px; margin-right: 16px; flex: none; }

  .brand-lockup {
    position: absolute; left: 390px; top: 196px; width: 170px;
    text-align: center; font-family: "Marcellus", serif;
  }
  .brand-lockup .brand-dot {
    display: block; width: 14px; height: 14px; margin: 0 auto 12px;
    border-radius: 50%; background: var(--gold);
  }
  .brand-lockup .brand-name { font-size: 21px; letter-spacing: 4px; }
  .brand-lockup .since { font-family: "Montserrat", sans-serif; font-size: 9px; letter-spacing: 2.5px; margin-top: 4px; }

  /* Brand side */
  .brand-face { text-align: center; font-family: "Marcellus", serif; }
  .brand-face .brand-name {
    position: absolute; left: 0; right: 0; top: 150px;
    font-size: 46px; letter-spacing: 9px;
  }
  .brand-face .since {
    position: absolute; left: 0; right: 0; top: 233px;
    font-family: "Montserrat", sans-serif; font-size: 15px; letter-spacing: 6px; color: var(--gold-soft);
  }

  .card.front-flat { left: 0; top: 0; }
  .card.back-flat { left: 602px; top: 0; width: 598px; }

  .stage {
    position: absolute; left: 0; top: 400px; width: 1200px; height: 664px;
    background: var(--stage-bg);
  }
  .stage .card { transform-origin: top left; transform: scale(0.8); box-shadow: 0 10px 24px rgba(0,0,0,0.45); }
  .stage .back-flat { left: 95px; top: 160px; width: 596px; }
  .stage .front-flat { left: 628px; top: 160px; }
</style>
</head>
<body>
<div class="canvas">

  <section class="card front-flat">
    <div class="card-frame"></div>
    <h1 class="company-title">KORBALT HAUGEN</h1>
    <p class="role">CEO &amp; Founder</p>
    <p class="person">Anders Lund Haugen</p>
    <ul class="contacts">
      <li><svg viewBox="0 0 24 24" fill="none" stroke="currentColor" stroke-width="1.8"><rect x="6" y="2" width="12" height="20" rx="2"/><line x1="11" y1="18.5" x2="13" y2="18.5"/></svg>004790412675</li>
      <li><svg viewBox="0 0 24 24" fill="none" stroke="currentColor" stroke-width="1.8"><rect x="2" y="5" width="20" height="14"/><path d="M2 5l10 8 10-8M2 19l7-7M22 19l-7-7"/></svg>korbalt.llc@mailpost.com</li>
      <li><svg viewBox="0 0 24 24" fill="none" stroke="currentColor" stroke-width="1.6"><circle cx="12" cy="12" r="10"/><ellipse cx="12" cy="12" rx="4.5" ry="10"/><line x1="2" y1="12" x2="22" y2="12"/><path d="M4 7h16M4 17h16"/></svg>www.korbalt.llc</li>
    </ul>
    <div class="brand-lockup">
      <span class="brand-dot"></span>
      <div class="brand-name">KORBALT</div>
      <div class="since">SINCE 2026</div>
    </div>
  </section>

  <section class="card back-flat brand-face">
    <div class="card-frame"></div>
    <div class="brand-name">KORBALT</div>
    <div class="since">SINCE 2026</div>
  </section>

  <div class="stage">
    <section class="card back-flat brand-face">
      <div class="card-frame"></div>
      <div class="brand-name">KORBALT</div>
      <div class="since">SINCE 2026</div>
    </section>

    <section class="card front-flat">
      <div class="card-frame"></div>
      <h1 class="company-title">KORBALT HAUGEN</h1>
      <p class="role">CEO &amp; Founder</p>
      <p class="person">Anders Lund Haugen</p>
      <ul class="contacts">
        <li><svg viewBox="0 0 24 24" fill="none" stroke="currentColor" stroke-width="1.8"><rect x="6" y="2" width="12" height="20" rx="2"/><line x1="11" y1="18.5" x2="13" y2="18.5"/></svg>004790412675</li>
        <li><svg viewBox="0 0 24 24" fill="none" stroke="currentColor" stroke-width="1.8"><rect x="2" y="5" width="20" height="14"/><path d="M2 5l10 8 10-8M2 19l7-7M22 19l-7-7"/></svg>korbalt.llc@mailpost.com</li>
        <li><svg viewBox="0 0 24 24" fill="none" stroke="currentColor" stroke-width="1.6"><circle cx="12" cy="12" r="10"/><ellipse cx="12" cy="12" rx="4.5" ry="10"/><line x1="2" y1="12" x2="22" y2="12"/><path d="M4 7h16M4 17h16"/></svg>www.korbalt.llc</li>
      </ul>
      <div class="brand-lockup">
        <span class="brand-dot"></span>
        <div class="brand-name">KORBALT</div>
        <div class="since">SINCE 2026</div>
      </div>
    </section>
  </div>

</div>
</body>
</html>
```